New Zealand Luggage Importer Needs Business Cards

We need professional, creative and fashionable business cards created.
We are based in New Zealand and import and distribute high-end, quality, fashionable and durable luggage.
We pride ourselves on selling the very best quality luggage, second only to 1 brand (which we won't mention here)...we use the same manufacturer. However, our prices are much more reasonable.
Industry/Entity Type
Business
Contact Information for Business Card
Mark Dunsley
027 512 4068
3/17 Harlow Street, Pinecrest Flats, Auckland, 0614
PO Box 204377, Fernside, Auckland 0731
09-528-3916
sales@brivancases.co.nz / www.brivancases.co.nz

```html
<!DOCTYPE html>
<html lang="en">
<head>
<meta charset="utf-8">
<title>Brivan Cases – Business Cards</title>
<link href="https://fonts.googleapis.com/css2?family=Open+Sans:wght@400;600;700&display=swap" rel="stylesheet">
<style>
  :root {
    --canvas: #cdcccc;
    --card: #060606;
    --band: #262423;
    --white: #ffffff;
    --text: #f1f1f1;
    --gold: #c9a45c;
    --rule: #8a8a8a;
  }
  * { box-sizing: border-box; margin: 0; padding: 0; }
  html, body { width: 750px; height: 1200px; overflow: hidden; }
  body {
    background: var(--canvas);
    font-family: "Open Sans", Arial, sans-serif;
    color: var(--text);
    position: relative;
  }
  .card {
    position: absolute;
    left: 120px;
    width: 506px;
    height: 319px;
    background: var(--card);
    overflow: hidden;
    box-shadow: 0 16px 20px rgba(0,0,0,0.14);
  }
  .card--front { top: 46px; }
  .card--back { top: 440px; }
  .card--vertical { top: 814px; }

  .light-streaks {
    position: absolute;
    inset: 0;
    background:
      radial-gradient(ellipse 140px 60px at 60px 110px, rgba(230,170,80,0.55), transparent 70%),
      radial-gradient(ellipse 260px 40px at 150px 70px, rgba(210,150,60,0.35), transparent 75%),
      radial-gradient(ellipse 200px 30px at 300px 40px, rgba(200,140,60,0.25), transparent 75%),
      radial-gradient(ellipse 120px 120px at 20px 180px, rgba(170,110,40,0.35), transparent 75%),
      linear-gradient(160deg, rgba(120,80,30,0.3) 0%, transparent 45%);
  }

  .brand-name {
    position: absolute;
    font-weight: 600;
    color: var(--gold);
    text-transform: uppercase;
    letter-spacing: 3px;
    white-space: nowrap;
  }

  /* Front */
  .card--front .person-name {
    position: absolute; top: 16px; right: 48px;
    font-size: 18px; font-weight: 700; color: var(--white);
  }
  .card--front .brand-name {
    left: 0; right: 0; top: 140px; text-align: center; font-size: 30px;
  }
  .card--front .web {
    position: absolute; left: 0; right: 0; top: 181px;
    text-align: center; font-size: 12px; color: var(--text);
  }

  /* Back */
  .card--back .brand-name { left: 20px; top: 40px; font-size: 26px; }
  .card--back .person-name {
    position: absolute; left: 8px; top: 161px; width: 190px;
    text-align: center; white-space: nowrap;
    font-size: 22px; font-weight: 700; color: var(--white);
  }
  .card--back .divider {
    position: absolute; left: 206px; top: 118px;
    width: 1px; height: 128px; background: var(--rule);
  }
  .contact {
    position: absolute;
    width: 230px;
    font-size: 14px;
    line-height: 17.5px;
    list-style: none;
  }
  .contact li { position: relative; padding-left: 28px; }
  .contact .gap { margin-top: 15px; }
  .contact .gap-lg { margin-top: 17px; }
  .contact svg {
    position: absolute; left: 0; top: 3px;
    width: 12px; height: 12px;
    fill: none; stroke: var(--white); stroke-width: 1.4;
  }
  .contact svg.pin { width: 15px; height: 18px; left: -2px; top: 2px; fill: var(--white); stroke: none; }
  .card--back .contact { left: 237px; top: 91px; }

  /* Vertical */
  .side-band {
    position: absolute; left: 0; top: 0; width: 71px; height: 100%;
    background: var(--band);
  }
  .card--vertical .light-streaks { left: 71px; }
  .card--vertical .brand-name {
    left: 36px; top: 160px; font-size: 26px;
    transform: translate(-50%, -50%) rotate(-90deg);
  }
  .card--vertical .person-name {
    position: absolute; left: 234px; top: 47px;
    font-size: 21px; font-weight: 700; color: var(--white);
  }
  .card--vertical .contact { left: 206px; top: 91px; }
</style>
</head>
<body>

<svg width="0" height="0" style="position:absolute" aria-hidden="true">
  <defs>
    <symbol id="icon-pin" viewBox="0 0 15 18"><path d="M7.5 0C3.4 0 0 3.3 0 7.3 0 12 7.5 18 7.5 18S15 12 15 7.3C15 3.3 11.6 0 7.5 0zm0 10.2a3 3 0 1 1 0-6 3 3 0 0 1 0 6z"/></symbol>
    <symbol id="icon-phone" viewBox="0 0 12 12"><path d="M2 1.5l2 .2.8 2.3-1.2 1a7 7 0 0 0 3.4 3.4l1-1.2 2.3.8.2 2c-5 .6-9-3.4-8.5-8.5z"/></symbol>
    <symbol id="icon-mobile" viewBox="0 0 12 12"><rect x="3" y="1" width="6" height="10" rx="1"/><line x1="5" y1="9" x2="7" y2="9"/></symbol>
    <symbol id="icon-mail" viewBox="0 0 12 12"><rect x="1" y="2.5" width="10" height="7"/><path d="M1 2.5l5 4 5-4"/></symbol>
    <symbol id="icon-globe" viewBox="0 0 12 12"><circle cx="6" cy="6" r="5"/><ellipse cx="6" cy="6" rx="2.2" ry="5"/><line x1="1" y1="6" x2="11" y2="6"/></symbol>
  </defs>
</svg>

<section class="card card--front">
  <div class="light-streaks" role="img" aria-label="Golden light streaks sweeping across the dark card"></div>
  <p class="person-name">Mark Dunsley</p>
  <p class="brand-name">Brivan Cases</p>
  <p class="web">www.brivancases.co.nz</p>
</section>

<section class="card card--back">
  <div class="light-streaks" role="img" aria-label="Golden light streaks sweeping across the dark card"></div>
  <p class="brand-name">Brivan Cases</p>
  <p class="person-name">Mark Dunsley</p>
  <div class="divider"></div>
  <ul class="contact">
    <li><svg class="pin"><use href="#icon-pin"/></svg>3/17 Harlow Street, Pinecrest Flats, Auckland, 0614<br>PO Box 204377, Fernside, Auckland 0731</li>
    <li class="gap"><svg><use href="#icon-phone"/></svg>027 512 4068</li>
    <li><svg><use href="#icon-mobile"/></svg>09-528-3916</li>
    <li class="gap-lg"><svg><use href="#icon-mail"/></svg>sales@brivancases.co.nz</li>
    <li><svg><use href="#icon-globe"/></svg>www.brivancases.co.nz</li>
  </ul>
</section>

<section class="card card--vertical">
  <div class="side-band"></div>
  <div class="light-streaks" role="img" aria-label="Golden light streaks sweeping across the dark card"></div>
  <p class="brand-name">Brivan Cases</p>
  <p class="person-name">Mark Dunsley</p>
  <ul class="contact">
    <li><svg class="pin"><use href="#icon-pin"/></svg>3/17 Harlow Street, Pinecrest Flats, Auckland, 0614<br>PO Box 204377, Fernside, Auckland 0731</li>
    <li class="gap"><svg><use href="#icon-phone"/></svg>027 512 4068</li>
    <li><svg><use href="#icon-mobile"/></svg>09-528-3916</li>
    <li class="gap-lg"><svg><use href="#icon-mail"/></svg>sales@brivancases.co.nz</li>
    <li><svg><use href="#icon-globe"/></svg>www.brivancases.co.nz</li>
  </ul>
</section>

</body>
</html>
```